Kitchen Tools Infographic - Helpful Items for Healthy Home Meals

We are a weight loss company that provides holistic, natural nutrition programs to consumers -- you can see our web site at www.FernaluVita.com. We need a simple infographic to be shared on social media and via email. The topic for the infographic is "Equip Your Kitchen for Healthy Home Meals". We've outlined 5 groups of kitchen tools that are helpful for consumers to have for preparing home meals, and included some framing statistics emphasizing the weight management benefits of preparing meals versus eating out.

Target Market(s)

Women age 35-55

Industry/Entity Type

Health And Wellness

Font styles to use
Sans Serif

Colors
0292cd
9bcb3b

Requirements
Must have
• - FernaluVita Logo
• - Graphics summarizing statistic (weight gain)
• - Graphics showing groupings of kitchen tools
Should not have
• body scale graphics
• before/after graphics

```html
<!DOCTYPE html>
<html lang="en">
<head>
<meta charset="utf-8">
<title>Equip your kitchen for healthy home meals</title>
<link href="https://fonts.googleapis.com/css2?family=Share+Tech+Mono&family=Open+Sans:wght@400;700&family=Roboto+Condensed:wght@700&display=swap" rel="stylesheet">
<style>
  :root{
    --blue:#0292cd;
    --green:#9bcb3b;
    --dark:#333333;
    --ink:#222222;
    --orange:#f7941d;
    --panel:#ebebeb;
    --card:#e8e8e8;
    --card-edge:#b9b9b9;
    --muted:#5a5a5a;
    --white:#ffffff;
  }
  *{margin:0;padding:0;box-sizing:border-box}
  html,body{width:1200px;height:3000px;overflow:hidden;background:var(--white)}
  body{position:relative;font-family:"Open Sans",Arial,sans-serif}
  .band{position:absolute;left:0;width:1200px;background:var(--dark)}
  .band svg.corners{position:absolute;inset:0}
  .mono{font-family:"Share Tech Mono",monospace;position:absolute;white-space:nowrap;line-height:1;font-weight:400}
  .chip{padding:0 12px}
  .chip--green{background:var(--green);color:var(--dark)}
  .chip--blue{background:var(--blue);color:var(--dark)}
  .t-green{color:var(--green)}
  .t-blue{color:var(--blue)}
  .t-deep{color:#1d7fae}

  .hero{top:45px;height:330px}
  .tools{top:1530px;height:270px}

  .stats{position:absolute;left:60px;top:405px;width:1065px;height:1050px}

  .num{position:absolute;width:132px;height:132px;border-radius:50%;color:var(--white);
       font:700 72px/132px "Roboto Condensed",Arial,sans-serif;text-align:center}
  .tab{position:absolute;height:90px;border-radius:18px 18px 0 0;color:var(--white);
       font:700 78px/92px "Roboto Condensed",Arial,sans-serif;padding:0 24px}
  .bg-blue{background:var(--blue)}
  .bg-green{background:var(--green)}
  .card{position:absolute;height:180px;background:var(--card);border-radius:12px;
        box-shadow:6px 6px 0 var(--card-edge);padding:24px 40px}
  .card ul{list-style:none}
  .card li{font-size:21px;line-height:45px;color:var(--muted);display:flex;align-items:center;gap:18px}
  .icon{display:inline-block;width:48px;height:36px;border-radius:6px;background:#555;flex:none}
</style>
</head>
<body>

<header class="band hero">
  <svg class="corners" width="1200" height="330" viewBox="0 0 1200 330" aria-hidden="true">
    <polygon points="0,0 75,0 0,45" fill="var(--orange)"/>
    <polygon points="1110,0 1170,0 1200,18 1200,54" fill="var(--orange)"/>
    <polygon points="0,285 36,330 0,330" fill="var(--orange)"/>
    <polygon points="1200,270 1200,330 1155,330" fill="var(--orange)"/>
  </svg>
  <h1>
    <span class="mono" style="left:200px;top:78px;font-size:84px"><span class="chip chip--green">Equip</span> <span class="t-green">your kitchen</span></span>
    <span class="mono" style="left:90px;top:200px;font-size:80px"><span class="t-blue">for</span> <span class="t-deep">healthy</span> <span class="chip chip--blue">home meals</span></span>
  </h1>
</header>

<section class="stats" aria-label="Why cook at home">
  <svg width="1065" height="1050" viewBox="60 405 1065 1050">
    <rect x="60" y="405" width="1065" height="1050" fill="var(--panel)"/>
    <g fill="#c8c8c8" opacity=".8">
      <polygon points="150,735 225,705 225,1455 150,1455"/>
      <polygon points="195,570 300,525 300,1455 195,1455"/>
      <rect x="1020" y="1080" width="45" height="375"/>
      <rect x="990" y="1170" width="45" height="285" fill="#b5b5b5"/>
    </g>

    <text x="105" y="588" font-family="Open Sans,Arial,sans-serif" font-weight="700" font-size="30" fill="var(--blue)">Why Cook at Home?</text>
    <g font-family="Open Sans,Arial,sans-serif" font-weight="700" font-size="17" fill="var(--ink)">
      <text x="180" y="618">Those who eat out consume an average of</text>
      <text x="150" y="645">134 calories more per meal. Americans eat out an</text>
      <text x="150" y="672">average of 4.5 times per week, so those extra calories</text>
      <text x="150" y="699">can add up to substantial weight gain -- and give you a</text>
      <text x="150" y="726">reason to prepare your own meals.</text>
    </g>

    <!-- calories per meal / week ring -->
    <g transform="rotate(-85 915 720)">
      <circle cx="915" cy="720" r="118" fill="none" stroke="var(--green)" stroke-width="104" stroke-dasharray="106 635"/>
    </g>
    <g transform="rotate(-31 915 720)">
      <circle cx="915" cy="720" r="118" fill="none" stroke="var(--blue)" stroke-width="104" stroke-dasharray="625 116"/>
    </g>
    <g font-family="Open Sans,Arial,sans-serif" font-weight="700" fill="var(--white)" text-anchor="middle">
      <text x="976" y="629" font-size="26">100</text>
      <text x="825" y="806" font-size="30">600</text>
    </g>
    <text x="696" y="480" font-family="Open Sans,Arial,sans-serif" font-weight="700" font-size="24" fill="var(--green)">CALORIES PER MEAL</text>
    <polyline points="790,510 1020,510" fill="none" stroke="var(--green)" stroke-width="3"/>
    <circle cx="1024" cy="510" r="9" fill="var(--green)"/>
    <polyline points="620,912 650,900 850,900" fill="none" stroke="var(--blue)" stroke-width="3"/>
    <circle cx="855" cy="900" r="9" fill="var(--blue)"/>
    <text x="486" y="940" font-family="Open Sans,Arial,sans-serif" font-weight="700" font-size="24" fill="var(--blue)">CALORIES PER WEEK</text>
    <text x="555" y="978" font-family="Open Sans,Arial,sans-serif" font-weight="700" font-size="23" fill="var(--ink)">Excess Calories from Restaurant Meals</text>

    <!-- pounds gained ring -->
    <g transform="rotate(-8 570 1230)">
      <circle cx="570" cy="1230" r="126" fill="none" stroke="var(--blue)" stroke-width="120" stroke-dasharray="470 792"/>
    </g>
    <g transform="rotate(210 570 1230)">
      <circle cx="570" cy="1230" r="126" fill="none" stroke="var(--dark)" stroke-width="120" stroke-dasharray="232 792"/>
    </g>
    <g transform="rotate(318 570 1230)">
      <circle cx="570" cy="1230" r="126" fill="none" stroke="var(--green)" stroke-width="120" stroke-dasharray="68 792"/>
    </g>
    <g font-family="Open Sans,Arial,sans-serif" font-weight="700" fill="var(--white)" text-anchor="middle">
      <text x="478" y="1150" font-size="26">4.5 lbs</text>
      <text x="648" y="1160" font-size="22">1.4 lbs</text>
      <text x="575" y="1368" font-size="30">8.96 lbs</text>
    </g>
    <text x="150" y="1072" font-family="Open Sans,Arial,sans-serif" font-size="28" fill="var(--ink)">6 months</text>
    <polyline points="200,1090 240,1140 360,1140" fill="none" stroke="var(--ink)" stroke-width="3"/>
    <circle cx="365" cy="1140" r="9" fill="var(--ink)"/>
    <circle cx="712" cy="1158" r="9" fill="var(--green)"/>
    <polyline points="712,1158 750,1158 790,1185 830,1185" fill="none" stroke="var(--green)" stroke-width="3"/>
    <text x="850" y="1195" font-family="Open Sans,Arial,sans-serif" font-size="28" fill="var(--green)">2 months</text>
    <g font-family="Open Sans,Arial,sans-serif" font-weight="700" font-size="32" fill="var(--ink)" text-anchor="middle">
      <text x="920" y="1290">Pounds Gained</text>
      <text x="920" y="1328">from Restaurant Meals</text>
    </g>
    <circle cx="420" cy="1380" r="9" fill="var(--blue)"/>
    <polyline points="420,1380 240,1380 225,1405" fill="none" stroke="var(--blue)" stroke-width="3"/>
    <text x="215" y="1443" font-family="Open Sans,Arial,sans-serif" font-size="28" fill="var(--blue)">1 year</text>
  </svg>
</section>

<section class="band tools" aria-label="Kitchen tools">
  <svg class="corners" width="1200" height="270" viewBox="0 0 1200 270" aria-hidden="true">
    <polygon points="0,0 75,0 0,45" fill="var(--orange)"/>
    <polygon points="1110,0 1170,0 1200,18 1200,54" fill="var(--orange)"/>
    <polygon points="0,225 36,270 0,270" fill="var(--orange)"/>
    <polygon points="1200,210 1200,270 1155,270" fill="var(--orange)"/>
  </svg>
  <h2>
    <span class="mono" style="left:120px;top:65px;font-size:62px"><span class="chip chip--green">make healthy</span> <span class="t-green">eating easier</span></span>
    <span class="mono" style="left:210px;top:165px;font-size:62px"><span class="t-blue">with these</span> <span class="chip chip--blue">kitchen tools</span></span>
  </h2>
</section>

<article class="tool-group">
  <div class="card" style="left:150px;top:1890px;width:1035px">
    <ul>
      <li>essential for prepping meat and vegetables.<span class="icon" role="img" aria-label="Cutting board icon" style="margin-left:50px"></span></li>
      <li>go for quality to make chopping, dicing and slicing faster and easier.<span class="icon" role="img" aria-label="Knife icon" style="margin-left:140px"></span></li>
      <li>get the precision you need for perfect recipes and portion control.<span class="icon" role="img" aria-label="Kitchen scale icon" style="margin-left:130px"></span></li>
    </ul>
  </div>
  <div class="tab bg-blue" style="left:165px;top:1815px;width:255px">PREP:</div>
  <div class="num bg-blue" style="left:48px;top:1830px">1</div>
</article>

<article class="tool-group">
  <div class="card" style="left:45px;top:2220px;width:1005px">
    <ul>
      <li><span class="icon" role="img" aria-label="Blender icon"></span>make highly nutritious, healthy drinks from fruits and veggies.</li>
      <li><span class="icon" role="img" aria-label="Pressure cooker icon"></span>create single pot meals in 20 minutes or less.</li>
      <li><span class="icon" role="img" aria-label="Slow cooker icon"></span>cook delicious meals while you are at work.</li>
    </ul>
  </div>
  <div class="tab bg-green" style="left:800px;top:2130px;width:290px">TECH:</div>
  <div class="num bg-green" style="left:1050px;top:2145px">2</div>
</article>

<article class="tool-group">
  <div class="card" style="left:150px;top:2565px;width:1035px">
    <ul>
      <li>nonstick cooking surface allows you to cook without oil<span class="icon" role="img" aria-label="Nonstick pan icon" style="margin-left:30px"></span></li>
      <li>preserve nutrients and natural, fresh taste.<span class="icon" role="img" aria-label="Steamer icon" style="margin-left:10px"></span></li>
      <li>ideal for roasting vegetables in the oven or baking chicken and fish dishes<span class="icon" role="img" aria-label="Baking dish icon" style="margin-left:10px"></span></li>
    </ul>
  </div>
  <div class="tab bg-blue" style="left:165px;top:2490px;width:255px">COOK:</div>
  <div class="num bg-blue" style="left:48px;top:2500px">3</div>
</article>

</body>
</html>
```